Business Card Design Project - Tall Maple

We are looking for a new business card design. Our company name is Tall Maple Communication Solutions. Our primary function is to provide our clients with communication solutions. These solutions include commercial phone systems and T1 and Fiber Internet lines. Another major part of the business is cabling new buildings with CAT5 cable for both data and phone.

Industry/Entity Type

Communication

Requirements
Must have
• The cards need to be two sided and have some bleeding edge color.
Nice to have
• We are going to upload our current logo BUT we are not married to this logo. If you want to incorporate a re-designed logo with the new business card - please feel free to do so. We are looking for a new bold look that is very colorful yet professional.

```html
<!DOCTYPE html>
<html lang="en">
<head>
<meta charset="utf-8">
<title>Tall Maple Communication Solutions – Business Cards</title>
<link rel="stylesheet" href="https://fonts.googleapis.com/css2?family=Saira:wght@500;600;700&display=swap">
<style>
  :root {
    --page-bg: #ffffff;
    --card-white: #ffffff;
    --brand-blue: #245a8f;
    --brand-navy: #0f3f73;
    --wave-light: #3b70a6;
    --mark-faint: #1c4b7d;
    --text-light: #ffffff;
    --card-shadow: 0 6px 14px rgba(0, 0, 0, 0.35);
  }
  * { box-sizing: border-box; margin: 0; padding: 0; }
  html, body {
    width: 1200px;
    height: 900px;
    overflow: hidden;
    background: var(--page-bg);
    font-family: "Saira", "Arial", sans-serif;
  }
  .canvas { position: relative; width: 1200px; height: 900px; }

  .card {
    position: absolute;
    width: 600px;
    height: 380px;
    overflow: hidden;
    box-shadow: var(--card-shadow);
  }

  /* Front */
  .card-front { left: 90px; top: 60px; background: var(--card-white); }
  .front-brand {
    position: absolute;
    top: 90px;
    left: 0;
    width: 100%;
    display: flex;
    align-items: center;
    justify-content: center;
    gap: 18px;
  }
  .brand-dot {
    width: 62px;
    height: 62px;
    border-radius: 50%;
    background: var(--brand-navy);
  }
  .brand-name {
    font-weight: 700;
    font-size: 62px;
    line-height: 1;
    color: var(--brand-navy);
    letter-spacing: 0.5px;
  }
  .front-wave { position: absolute; left: 0; bottom: 0; width: 600px; height: 170px; }
  .tagline {
    position: absolute;
    left: 0;
    bottom: 32px;
    width: 100%;
    text-align: center;
    font-weight: 600;
    font-size: 33px;
    color: var(--text-light);
  }

  /* Back */
  .card-back { left: 480px; top: 470px; width: 630px; background: var(--card-white); }
  .back-field {
    position: absolute;
    inset: 0 0 36px 0;
    background: var(--brand-blue);
  }
  .back-brand {
    position: absolute;
    left: 42px;
    top: 118px;
    display: flex;
    align-items: center;
    gap: 14px;
  }
  .back-brand .brand-dot { width: 50px; height: 50px; background: var(--mark-faint); }
  .back-brand .brand-name { font-size: 46px; color: var(--mark-faint); }
  .divider {
    position: absolute;
    left: 328px;
    top: 48px;
    width: 2px;
    height: 236px;
    background: var(--text-light);
  }
  .contact {
    position: absolute;
    left: 348px;
    top: 52px;
    color: var(--text-light);
  }
  .contact-name { font-weight: 600; font-size: 29px; line-height: 1.1; margin-bottom: 22px; }
  .contact-address { font-weight: 500; font-size: 16px; line-height: 1.3; margin-bottom: 22px; }
  .contact-phones { list-style: none; font-weight: 500; font-size: 16px; line-height: 1.2; }
</style>
</head>
<body>
<main class="canvas">

  <section class="card card-front" aria-label="Card front">
    <div class="front-brand">
      <span class="brand-dot"></span>
      <span class="brand-name">Tall Maple</span>
    </div>
    <svg class="front-wave" viewBox="0 0 600 170" preserveAspectRatio="none" aria-hidden="true">
      <path d="M0 60 C120 -5 260 0 380 25 C470 45 540 50 600 40 L600 170 L0 170 Z" fill="var(--wave-light)"/>
      <path d="M0 80 C120 20 260 20 380 45 C470 62 540 66 600 58 L600 170 L0 170 Z" fill="var(--brand-blue)"/>
    </svg>
    <p class="tagline">Communication Solutions</p>
  </section>

  <section class="card card-back" aria-label="Card back">
    <div class="back-field"></div>
    <div class="back-brand">
      <span class="brand-dot"></span>
      <span class="brand-name">Tall Maple</span>
    </div>
    <div class="divider"></div>
    <div class="contact">
      <h1 class="contact-name">Nolan Pruitt</h1>
      <p class="contact-address">1480 W Ridgeline Avenue,<br>Suite 300 Mesa, AZ 85201</p>
      <ul class="contact-phones">
        <li>Office: 480.555.0142</li>
        <li>Cell: 480.555.0187</li>
        <li>24/7: 800.555.0163</li>
        <li>Fax: 800.555.0119</li>
      </ul>
    </div>
  </section>

</main>
</body>
</html>
```